Bref créative
Brivona Real Estate
Professional
Tom Radcliffe
President
782 W. Hollow Pine Rd. Suite 310
Beverly Hills, CA 90210
tom@BrivonaRealEstate.example
www.BrivonaRealEstate.example
I will upload our logo. If there is a problem with that please use logo on web site www.brivonarealestate.example
Please use our logo.

```html
<!DOCTYPE html>
<html lang="en">
<head>
<meta charset="utf-8">
<title>Brivona Real Estate – Business Card</title>
<link href="https://fonts.googleapis.com/css2?family=Arimo:wght@400;700&display=swap" rel="stylesheet">
<style>
  :root {
    --navy: #1b2f5c;
    --navy-deep: #0f1d3d;
    --accent-blue: #2f5da8;
    --text-dark: #2a2a2a;
    --card-light: #ffffff;
    --card-shade: #e4e6ea;
    --card-edge: #c9ccd2;
    --page: #ffffff;
  }
  * { box-sizing: border-box; margin: 0; padding: 0; }
  html, body {
    width: 1200px; height: 329px; overflow: hidden;
    background: var(--page);
    font-family: "Arimo", Arial, sans-serif;
  }
  .sheet { position: relative; width: 1200px; height: 329px; }
  .card {
    position: absolute; top: 2px; width: 578px; height: 325px;
    background: radial-gradient(ellipse at 40% 35%, var(--card-light) 0%, #f4f5f7 50%, var(--card-shade) 100%);
    border: 1px solid var(--card-edge);
    overflow: hidden;
  }
  .card--front { left: 0; }
  .card--back { left: 620px; }
  .swoosh { position: absolute; left: 0; top: 0; }
  .brand { position: absolute; left: 110px; top: 34px; }
  .brand__row { display: flex; align-items: center; gap: 12px; }
  .brand__mark { width: 26px; height: 26px; background: var(--navy); }
  .brand__name {
    font-weight: 700; font-size: 34px; letter-spacing: 1px;
    color: var(--navy); text-transform: uppercase; white-space: nowrap;
  }
  .brand__tagline {
    margin-top: 8px; margin-left: 38px;
    font-size: 13px; font-weight: 700; color: var(--accent-blue);
    letter-spacing: 0.5px; white-space: nowrap;
  }
  .contact {
    position: absolute; left: 29px; top: 206px;
    font-size: 11.5px; line-height: 15px; color: var(--text-dark);
  }
  .contact__label { color: var(--accent-blue); }
  .person { position: absolute; left: 432px; top: 240px; }
  .person__name { font-size: 17px; font-weight: 700; color: var(--accent-blue); }
  .person__title { font-size: 12px; color: var(--text-dark); margin-top: 2px; }
  .back-art {
    position: absolute; right: 0; bottom: 0; width: 260px; height: 230px;
    background: linear-gradient(180deg, rgba(200,206,216,0) 0%, rgba(190,198,210,0.45) 100%);
  }
</style>
</head>
<body>
<div class="sheet">

  <section class="card card--front">
    <svg class="swoosh" width="300" height="140" viewBox="0 0 300 140" aria-hidden="true">
      <path d="M0 0 H250 C170 10 80 40 0 125 Z" fill="var(--navy-deep)"/>
      <path d="M250 0 C170 10 80 40 0 125 V132 C85 50 175 16 265 0 Z" fill="var(--accent-blue)" opacity="0.55"/>
    </svg>
    <div class="brand">
      <div class="brand__row">
        <span class="brand__mark"></span>
        <span class="brand__name">Brivona Real Estate</span>
      </div>
      <div class="brand__tagline">Investments • Brokerage • Solutions</div>
    </div>
    <address class="contact" style="font-style:normal">
      782 W. Hollow Pine Rd. Suite 310<br>
      Beverly Hills, CA 90210<br>
      <span class="contact__label">Phone :</span> 310-555-0148<br>
      <span class="contact__label">Cell :</span> 310-555-0192<br>
      <span class="contact__label">Fax :</span> 866-555-0173<br>
      <span class="contact__label">Email :</span> tom@BrivonaRealEstate.example<br>
      <span class="contact__label">Web :</span> www.BrivonaRealEstate.example
    </address>
    <div class="person">
      <div class="person__name">Tom Radcliffe</div>
      <div class="person__title">President</div>
    </div>
  </section>

  <section class="card card--back">
    <svg class="swoosh" width="300" height="140" viewBox="0 0 300 140" aria-hidden="true">
      <path d="M0 0 H250 C170 10 80 40 0 125 Z" fill="var(--navy-deep)"/>
      <path d="M250 0 C170 10 80 40 0 125 V132 C85 50 175 16 265 0 Z" fill="var(--accent-blue)" opacity="0.55"/>
    </svg>
    <div class="brand">
      <div class="brand__row">
        <span class="brand__mark"></span>
        <span class="brand__name">Brivona Real Estate</span>
      </div>
      <div class="brand__tagline">Investments • Brokerage • Solutions</div>
    </div>
    <div class="back-art" role="img" aria-label="Faint city skyline decoration"></div>
  </section>

</div>
</body>
</html>
```